"Broadcast Tinkerings" - podcast cover artwrok

I need podcast cover artwork for "Broadcast Tinkerings". As the name implies, it focuses on experimenting with podcasts. I started this podcast a couple years ago and am rebranding now (old name was "Lantern Workshop" with the tagline of "broadcast tinkerings).

Maybe have (in small type) "a production of Harbor Finch Audio, LLC".

I would like it to convey creativity, innovation, and simplicity.

UPDATE: I uploaded a couple other podcast artwork I like to help with inspiration.

Target Market(s)

Podcasters, bloggers, entrepreneurs

Font styles to use
Sans Serif

Colors
0355a3
acd036
faa54b

Requirements
Must have
• Colors I like are darker shades of blue, green, and tan/sand. I selected sample colors, but the shade can vary to ensure that they are complementary.
Nice to have
• I've included a cartoon image of myself that may or may not work with the design.

```html
<!DOCTYPE html>
<html lang="en">
<head>
<meta charset="utf-8">
<title>Broadcast Tinkerings – Podcast Cover</title>
<link href="https://fonts.googleapis.com/css2?family=Fredoka:wght@500;600;700&display=swap" rel="stylesheet">
<style>
  :root {
    --brand-blue: #0355a3;
    --brand-blue-deep: #023a70;
    --brand-green: #acd036;
    --brand-green-deep: #5f8f14;
    --brand-sand: #faa54b;
    --brand-sand-light: #f6d3a2;
    --title-green: #62bf1e;
    --title-edge: #ffffff;
    --title-shadow: #1f3d0c;
    --paper: #fbfaf5;
    --portrait-tone: #f3c99a;
    --portrait-ring: #fff4e6;
    --mark-ink: #2b2b2b;
    --credit-ink: #023a70;
  }
  * { margin: 0; padding: 0; box-sizing: border-box; }
  html, body { width: 1200px; height: 1187px; overflow: hidden; background: var(--paper); }
  .cover {
    position: relative;
    width: 1200px;
    height: 1187px;
    overflow: hidden;
    background: var(--paper);
    font-family: "Fredoka", "Arial Rounded MT Bold", sans-serif;
  }
  .smoke-art {
    position: absolute;
    inset: 0;
    background:
      radial-gradient(ellipse 260px 220px at 1140px 60px, var(--brand-green), transparent 75%),
      radial-gradient(ellipse 340px 250px at 880px 140px, var(--brand-sand-light), transparent 75%),
      radial-gradient(ellipse 420px 300px at 560px 220px, var(--brand-sand), transparent 72%),
      radial-gradient(ellipse 380px 260px at 800px 340px, #e88a2a, transparent 72%),
      radial-gradient(ellipse 300px 430px at 110px 420px, var(--brand-blue), transparent 75%),
      radial-gradient(ellipse 240px 360px at 50px 720px, var(--brand-blue-deep), transparent 75%),
      radial-gradient(ellipse 360px 300px at 420px 910px, var(--brand-green-deep), transparent 72%),
      radial-gradient(ellipse 320px 240px at 580px 560px, #f08f2e, transparent 70%),
      linear-gradient(180deg, #dfe9f3 0%, var(--paper) 85%);
  }
  .portrait {
    position: absolute;
    left: 396px;
    top: 302px;
    width: 398px;
    height: 398px;
    border-radius: 50%;
    background: radial-gradient(circle at 50% 45%, var(--portrait-tone), #e0a266 80%);
    border: 14px solid var(--portrait-ring);
  }
  .show-title {
    position: absolute;
    left: 0;
    top: 0;
    width: 1200px;
    height: 1187px;
    filter: drop-shadow(0 12px 14px rgba(0,0,0,0.4));
  }
  .show-title text {
    font-family: "Fredoka", "Arial Rounded MT Bold", sans-serif;
    font-weight: 700;
    fill: var(--title-green);
    stroke: var(--title-edge);
    stroke-width: 5px;
    paint-order: stroke fill;
  }
  .show-title .title-shadow { fill: var(--title-shadow); stroke: var(--title-shadow); }
  .network-mark {
    position: absolute;
    left: 0;
    top: 0;
    width: 1200px;
    height: 1187px;
  }
  .network-mark text {
    font-family: "Fredoka", "Arial Rounded MT Bold", sans-serif;
    font-weight: 600;
    fill: var(--mark-ink);
  }
  .production-credit {
    position: absolute;
    left: 40px;
    bottom: 26px;
    font-family: "Fredoka", "Arial Rounded MT Bold", sans-serif;
    font-weight: 500;
    font-size: 20px;
    letter-spacing: 0.5px;
    color: var(--credit-ink);
  }
</style>
</head>
<body>
  <main class="cover">
    <div class="smoke-art" role="img" aria-label="Bursting clouds of blue, green and sand coloured smoke with a golden sunburst behind the host"></div>
    <div class="portrait" role="img" aria-label="Cartoon portrait of the smiling host in a round frame"></div>

    <svg class="show-title" viewBox="0 0 1200 1187" aria-labelledby="show-title-text">
      <title id="show-title-text">Broadcast Tinkerings</title>
      <g class="title-shadow" aria-hidden="true">
        <text x="216" y="741" font-size="170" textLength="750" lengthAdjust="spacingAndGlyphs">Broadcast</text>
        <text x="199" y="888" font-size="170" textLength="838" lengthAdjust="spacingAndGlyphs">Tinkerings</text>
      </g>
      <text x="216" y="733" font-size="170" textLength="750" lengthAdjust="spacingAndGlyphs">Broadcast</text>
      <text x="199" y="880" font-size="170" textLength="838" lengthAdjust="spacingAndGlyphs">Tinkerings</text>
    </svg>

    <svg class="network-mark" viewBox="0 0 1200 1187" aria-label="The Signal Almanac with Rowan Pell">
      <text x="925" y="1000" font-size="40">The</text>
      <text x="905" y="1060" font-size="62" textLength="270" lengthAdjust="spacingAndGlyphs">SIGNAL</text>
      <text x="915" y="1115" font-size="54" textLength="250" lengthAdjust="spacingAndGlyphs">ALMANAC</text>
      <text x="940" y="1145" font-size="20" textLength="200" lengthAdjust="spacingAndGlyphs">WITH ROWAN PELL</text>
    </svg>

    <p class="production-credit">a production of Harbor Finch Audio, LLC</p>
  </main>
</body>
</html>
```